Tradeline Summit & Fair xmas banner/MREC promotion

Size:
• Leader board: 728 x 90 px
• MREC: 300 x250 px
• Half-page: 300 x 600
• Wide skyscraper: 160 x 600
Image:
Candy cane stripes as the background – image bought. Horizontal or vertical whatever you think will works.
White strip/background for the copy? See images example – unless you don’t need to do that?
Bold font which is "neutra" to our other banners attached. I think black font would look good.
Message:
Please give it a good readable pace between slides – 3 secs?
1st Slide
It’s silly season!
2nd Slide
Treat yourself to an end of year gift
3rd Slide
Book your ticket now and save $$$
4th Slide
Get spoilt. You’re worth it!
5th Slide
Tradeline logo
Target Market(s)
anyone that sells online
• Automotive • Advertising • Digital • Entertainment
• Finance • Hospitality • Pharmaceutical/Healthcare • Pop Culture
• Retail • Travel • Telecommunications

```html
<!DOCTYPE html>
<html lang="en">
<head>
<meta charset="utf-8">
<title>Tradeline Summit &amp; Fair – Holiday Half-Page Banners</title>
<link rel="stylesheet" href="https://fonts.googleapis.com/css2?family=Josefin+Sans:wght@700&display=swap">
<style>
  :root {
    --canvas: #ffffff;
    --ink: #0a0a0a;
    --frame: #1a1a1a;
    --strip-top: #f6f6f6;
    --strip-bottom: #ffffff;
    --candy-red: #d42a3c;
    --candy-deep: #b01f3a;
    --candy-white: #f1e9ea;
  }
  * { box-sizing: border-box; margin: 0; padding: 0; }
  html, body {
    width: 1200px;
    height: 1000px;
    overflow: hidden;
    background: var(--canvas);
  }
  .banner-set {
    position: relative;
    width: 1200px;
    height: 1000px;
  }
  .banner {
    position: absolute;
    top: 180px;
    width: 300px;
    height: 600px;
    border: 1px solid var(--frame);
    overflow: hidden;
    display: flex;
    flex-direction: column;
    background: var(--canvas);
  }
  .banner--slide-1 { left: 60px; }
  .banner--slide-2 { left: 449px; }
  .banner--slide-3 { left: 837px; }

  .candy-photo {
    flex: 0 0 185px;
    background:
      linear-gradient(180deg,
        var(--candy-deep) 0%, var(--candy-white) 14%, var(--candy-red) 30%,
        var(--candy-white) 46%, var(--candy-red) 62%, var(--candy-white) 78%,
        var(--candy-deep) 100%);
  }
  .candy-photo--bottom { flex-basis: 186px; }

  .copy-strip {
    flex: 1 1 auto;
    background: linear-gradient(180deg, var(--strip-top), var(--strip-bottom));
    display: flex;
    flex-direction: column;
    align-items: center;
    justify-content: center;
    text-align: center;
    font-family: "Josefin Sans", "Century Gothic", sans-serif;
    font-weight: 700;
    color: var(--ink);
    text-transform: uppercase;
  }
  .headline {
    font-size: 35px;
    line-height: 44px;
    letter-spacing: 0.5px;
  }
  .headline--lead { font-size: 34px; line-height: 44px; margin-bottom: 10px; }
  .headline--large { font-size: 40px; line-height: 44px; }

  .brand {
    text-transform: none;
    display: flex;
    flex-direction: column;
    align-items: flex-end;
    line-height: 1;
  }
  .brand__name { font-size: 40px; letter-spacing: 0.5px; }
  .brand__tagline { font-size: 14px; margin-top: 4px; }
</style>
</head>
<body>
<main class="banner-set">

  <section class="banner banner--slide-1">
    <div class="candy-photo" role="img" aria-label="Close-up of red and white candy cane stripes"></div>
    <div class="copy-strip">
      <p class="headline">It’s<br>Silly Season!</p>
    </div>
    <div class="candy-photo candy-photo--bottom" role="img" aria-label="Close-up of red and white candy cane stripes"></div>
  </section>

  <section class="banner banner--slide-2">
    <div class="candy-photo" role="img" aria-label="Close-up of red and white candy cane stripes"></div>
    <div class="copy-strip">
      <p class="headline headline--lead">Get Spoilt.</p>
      <p class="headline headline--large">You’re<br>Worth It!</p>
    </div>
    <div class="candy-photo candy-photo--bottom" role="img" aria-label="Close-up of red and white candy cane stripes"></div>
  </section>

  <section class="banner banner--slide-3">
    <div class="candy-photo" role="img" aria-label="Close-up of red and white candy cane stripes"></div>
    <div class="copy-strip">
      <p class="brand">
        <span class="brand__name">Tradeline</span>
        <span class="brand__tagline">Summit &amp; Fair</span>
      </p>
    </div>
    <div class="candy-photo candy-photo--bottom" role="img" aria-label="Close-up of red and white candy cane stripes"></div>
  </section>

</main>
</body>
</html>
```